Finance cashflow waterfall graphic

Recreate "Cashflow Waterfall Example 1" - waterfall term used to explain the different accounts and priority that need to be paid as part of a apartment building / project. Create simple, business professional graphic for real estate report. Check the inspiration image but change to dorm building, no people - potentially combine the two images... Ideally editable so I can change the names of the accounts / colors / etc.

```html
<!DOCTYPE html>
<html lang="en">
<head>
<meta charset="utf-8">
<title>Finance Cashflow Waterfall</title>
<link href="https://fonts.googleapis.com/css2?family=Poppins:wght@300;600&display=swap" rel="stylesheet">
<style>
  :root {
    --page-bg: #e6e7e9;
    --card-bg: #ffffff;
    --ink: #111111;
    --flow: #8fd3f5;
    --flow-mark: #e4f5fd;
    --accent-line: #2bb3ec;
    --step-1: #5ab4e5;
    --step-2: #1e8fcf;
    --step-3: #2f6f8f;
    --step-4: #1e5f6a;
    --step-5: #17514f;
    --step-6: #154e58;
    --step-7: #0f4545;
    --step-8: #03262d;
    --tap: #f47f52;
    --building: #f4925a;
  }
  html, body {
    margin: 0;
    width: 1200px;
    height: 1200px;
    overflow: hidden;
    background: var(--page-bg);
  }
  .canvas {
    width: 1200px;
    height: 1200px;
    display: flex;
    align-items: center;
    justify-content: center;
  }
  .waterfall-card {
    display: block;
    width: 1200px;
    height: 1067px;
    background: var(--card-bg);
  }
  .card-title {
    font-family: "Poppins", sans-serif;
    font-weight: 300;
    font-size: 40px;
    fill: var(--ink);
  }
  .step-label {
    font-family: "Poppins", sans-serif;
    font-weight: 600;
    font-size: 17px;
    fill: var(--ink);
  }
  .step-label.left { text-anchor: end; }
  .step-number {
    font-family: "Poppins", sans-serif;
    font-weight: 300;
    font-size: 44px;
    fill: #ffffff;
    text-anchor: middle;
  }
  .flow-band {
    fill: none;
    stroke: var(--flow);
    stroke-width: 30;
    stroke-linejoin: round;
  }
  .flow-arrow {
    fill: none;
    stroke: var(--flow-mark);
    stroke-width: 2;
  }
  .flow-arrow-head { fill: var(--flow-mark); }
  .flow-dollar {
    font-family: "Poppins", sans-serif;
    font-weight: 600;
    font-size: 18px;
    fill: var(--flow-mark);
    text-anchor: middle;
  }
  .step-accent {
    fill: none;
    stroke: var(--accent-line);
    stroke-width: 2.5;
  }
</style>
</head>
<body>
<main class="canvas">
  <svg class="waterfall-card" viewBox="0 0 1043 927" xmlns="http://www.w3.org/2000/svg" aria-labelledby="chart-title">
    <title id="chart-title">Finance cashflow waterfall</title>
    <defs>
      <linearGradient id="accent-fade-left" x1="1" x2="0" y1="0" y2="0">
        <stop offset="0" stop-color="var(--accent-line)"/>
        <stop offset="1" stop-color="var(--accent-line)" stop-opacity="0"/>
      </linearGradient>
      <linearGradient id="accent-fade-right" x1="0" x2="1" y1="0" y2="0">
        <stop offset="0" stop-color="var(--accent-line)"/>
        <stop offset="1" stop-color="var(--accent-line)" stop-opacity="0"/>
      </linearGradient>
    </defs>

    <!-- Tap and building artwork areas -->
    <rect class="tap-art" x="515" y="40" width="225" height="207" rx="24" fill="var(--tap)" role="img" aria-label="Orange water tap pouring cash from the building"/>
    <rect class="building-art" x="790" y="96" width="202" height="759" fill="var(--building)" role="img" aria-label="Orange multi-storey dorm building with blue windows"/>

    <!-- Title -->
    <text class="card-title" x="250" y="190">FINANCE</text>
    <text class="card-title" x="250" y="230">CASHFLOW</text>

    <!-- Flow ribbon -->
    <g class="flow">
      <path class="flow-band" d="M548 245 L548 275 C548 302 470 312 400 324 L286 347"/>
      <path class="flow-band" d="M286 347 L537 418 L283 493 L537 562 L283 630 L537 706 L283 775 L537 844"/>

      <g class="flow-arrows">
        <line class="flow-arrow" x1="492" y1="302" x2="382" y2="318"/><polygon class="flow-arrow-head" points="375,319 390,311 389,325"/>
        <line class="flow-arrow" x1="348" y1="377" x2="460" y2="391"/><polygon class="flow-arrow-head" points="468,392 453,384 452,398"/>
        <line class="flow-arrow" x1="470" y1="449" x2="356" y2="464"/><polygon class="flow-arrow-head" points="348,465 363,457 362,471"/>
        <line class="flow-arrow" x1="348" y1="518" x2="460" y2="532"/><polygon class="flow-arrow-head" points="468,533 453,525 452,539"/>
        <line class="flow-arrow" x1="470" y1="590" x2="356" y2="605"/><polygon class="flow-arrow-head" points="348,606 363,598 362,612"/>
        <line class="flow-arrow" x1="348" y1="660" x2="460" y2="674"/><polygon class="flow-arrow-head" points="468,675 453,667 452,681"/>
        <line class="flow-arrow" x1="470" y1="734" x2="356" y2="749"/><polygon class="flow-arrow-head" points="348,750 363,742 362,756"/>
        <line class="flow-arrow" x1="348" y1="802" x2="460" y2="816"/><polygon class="flow-arrow-head" points="468,817 453,809 452,823"/>
      </g>

      <g class="flow-dollars">
        <text class="flow-dollar" x="548" y="282" font-size="24">$</text>
        <text class="flow-dollar" x="522" y="300" transform="rotate(-30 522 294)">$</text>
        <text class="flow-dollar" x="347" y="330" transform="rotate(-30 347 324)">$</text>
        <text class="flow-dollar" x="330" y="380" transform="rotate(-70 330 374)">$</text>
        <text class="flow-dollar" x="486" y="402" transform="rotate(-30 486 396)">$</text>
        <text class="flow-dollar" x="488" y="452" transform="rotate(-70 488 446)">$</text>
        <text class="flow-dollar" x="330" y="476" transform="rotate(-30 330 470)">$</text>
        <text class="flow-dollar" x="330" y="522" transform="rotate(-70 330 516)">$</text>
        <text class="flow-dollar" x="486" y="546" transform="rotate(-30 486 540)">$</text>
        <text class="flow-dollar" x="488" y="593" transform="rotate(-70 488 587)">$</text>
        <text class="flow-dollar" x="330" y="614" transform="rotate(-30 330 608)">$</text>
        <text class="flow-dollar" x="330" y="664" transform="rotate(-70 330 658)">$</text>
        <text class="flow-dollar" x="486" y="690" transform="rotate(-30 486 684)">$</text>
        <text class="flow-dollar" x="488" y="737" transform="rotate(-70 488 731)">$</text>
        <text class="flow-dollar" x="330" y="758" transform="rotate(-30 330 752)">$</text>
        <text class="flow-dollar" x="330" y="806" transform="rotate(-70 330 800)">$</text>
        <text class="flow-dollar" x="486" y="830" transform="rotate(-30 486 824)">$</text>
      </g>
    </g>

    <!-- Left-side steps -->
    <g class="step step-left">
      <path class="step-accent" stroke="url(#accent-fade-left)" d="M290 303 C270 300 250 301 200 301"/>
      <path class="step-accent" stroke="url(#accent-fade-left)" d="M290 391 C270 394 250 393 200 393"/>
      <circle cx="286" cy="347" r="38" fill="var(--step-1)"/>
      <text class="step-number" x="286" y="363">1</text>
      <text class="step-label left" x="223" y="349">Revenue</text>
    </g>
    <g class="step step-left">
      <path class="step-accent" stroke="url(#accent-fade-left)" d="M287 449 C267 446 247 447 197 447"/>
      <path class="step-accent" stroke="url(#accent-fade-left)" d="M287 537 C267 540 247 539 197 539"/>
      <circle cx="283" cy="493" r="38" fill="var(--step-3)"/>
      <text class="step-number" x="283" y="509">3</text>
      <text class="step-label left" x="223" y="485">Debt</text>
      <text class="step-label left" x="223" y="505">Payment</text>
    </g>
    <g class="step step-left">
      <path class="step-accent" stroke="url(#accent-fade-left)" d="M287 586 C267 583 247 584 197 584"/>
      <path class="step-accent" stroke="url(#accent-fade-left)" d="M287 674 C267 677 247 676 197 676"/>
      <circle cx="283" cy="630" r="38" fill="var(--step-5)"/>
      <text class="step-number" x="283" y="646">5</text>
      <text class="step-label left" x="223" y="627">Recapitalization</text>
      <text class="step-label left" x="223" y="647">Accounts</text>
    </g>
    <g class="step step-left">
      <path class="step-accent" stroke="url(#accent-fade-left)" d="M287 731 C267 728 247 729 197 729"/>
      <path class="step-accent" stroke="url(#accent-fade-left)" d="M287 819 C267 822 247 821 197 821"/>
      <circle cx="283" cy="775" r="38" fill="var(--step-7)"/>
      <text class="step-number" x="283" y="791">7</text>
      <text class="step-label left" x="223" y="762">Sustainment</text>
      <text class="step-label left" x="223" y="782">Reserves / Member</text>
      <text class="step-label left" x="223" y="802">Distribution (60%)</text>
    </g>

    <!-- Right-side steps -->
    <g class="step step-right">
      <path class="step-accent" stroke="url(#accent-fade-right)" d="M533 374 C553 371 573 372 633 372"/>
      <path class="step-accent" stroke="url(#accent-fade-right)" d="M533 462 C553 465 573 464 633 464"/>
      <circle cx="537" cy="418" r="38" fill="var(--step-2)"/>
      <text class="step-number" x="537" y="434">2</text>
      <text class="step-label" x="594" y="413">Operating</text>
      <text class="step-label" x="594" y="433">Expenses</text>
    </g>
    <g class="step step-right">
      <path class="step-accent" stroke="url(#accent-fade-right)" d="M533 518 C553 515 573 516 633 516"/>
      <path class="step-accent" stroke="url(#accent-fade-right)" d="M533 606 C553 609 573 608 633 608"/>
      <circle cx="537" cy="562" r="38" fill="var(--step-4)"/>
      <text class="step-number" x="537" y="578">4</text>
      <text class="step-label" x="594" y="546">Asset</text>
      <text class="step-label" x="594" y="566">Management</text>
      <text class="step-label" x="594" y="586">Fees</text>
    </g>
    <g class="step step-right">
      <path class="step-accent" stroke="url(#accent-fade-right)" d="M533 662 C553 659 573 660 633 660"/>
      <path class="step-accent" stroke="url(#accent-fade-right)" d="M533 750 C553 753 573 752 633 752"/>
      <circle cx="537" cy="706" r="38" fill="var(--step-6)"/>
      <text class="step-number" x="537" y="722">6</text>
      <text class="step-label" x="594" y="698">Incentive</text>
      <text class="step-label" x="594" y="718">Fees</text>
    </g>
    <g class="step step-right">
      <path class="step-accent" stroke="url(#accent-fade-right)" d="M533 800 C553 797 573 798 633 798"/>
      <path class="step-accent" stroke="url(#accent-fade-right)" d="M533 888 C553 891 573 890 633 890"/>
      <circle cx="537" cy="844" r="38" fill="var(--step-8)"/>
      <text class="step-number" x="537" y="860">8</text>
      <text class="step-label" x="594" y="830">Private Returns /</text>
      <text class="step-label" x="594" y="850">Managing Member</text>
      <text class="step-label" x="594" y="870">Distribution (40%)</text>
    </g>
  </svg>
</main>
</body>
</html>
```